Homepage Real Estate Agency

I need a web design for a real estate agency in Luxembourg. A short draft for the front page can be found in the project details. (Page 1+2) The main colors of the site should be blue as shown in the project details. (Page 3)
The main target for this site is to promote real estates and a small presentation of the company.

Industry/Entity Type

Real Estate

Requirements
Must have
• On the front page estates are shown in a short preview in small boxes, on the right side is a search. The search is hidden except for the front page. The header has 4 buttons and the logo of the company.

```html
<!DOCTYPE html>
<html lang="en">
<head>
<meta charset="utf-8">
<title>Clairvaux Homes – Real Estate Luxembourg</title>
<link href="https://fonts.googleapis.com/css2?family=Arimo:wght@400;700&family=Vollkorn:wght@400;600&display=swap" rel="stylesheet">
<style>
:root{
  --page-bg:#b9b9b9;
  --nav-dark:#1c1c1c;
  --nav-mid:#2f2f2f;
  --slate:#4b5a7a;
  --slate-dark:#3a4766;
  --slate-light:#6a7898;
  --title-blue:#56627f;
  --text:#444;
  --white:#fff;
  --panel:#f7f7f7;
  --dark-panel:#2b2b2b;
  --accent-red:#e2141b;
  --rss:#f0892a;
}
*{box-sizing:border-box;margin:0;padding:0}
html,body{width:1200px;height:900px;overflow:hidden}
body{position:relative;background:var(--page-bg);font-family:"Arimo",Arial,sans-serif;color:var(--text)}
.abs{position:absolute}
.brand{left:280px;top:30px;display:flex;align-items:center;gap:10px;font-family:"Vollkorn",serif;font-weight:600;font-size:22px;color:var(--slate-dark)}
.brand-dot{width:26px;height:26px;border-radius:50%;background:var(--slate-dark)}
.search-tab{left:741px;top:70px;width:178px;height:34px;background:var(--slate-dark);border-radius:8px 8px 0 0;padding:7px 0 0 9px;display:flex;gap:6px}
.search-tab .field{width:138px;height:14px;background:var(--white);font-size:8px;color:#999;padding:2px 4px}
.search-tab .go{color:var(--white);font-size:8px;font-weight:700;line-height:14px}
.main-nav{left:277px;top:95px;width:645px;height:32px;background:linear-gradient(#3a3a3a,var(--nav-dark));display:flex;align-items:center;padding-left:9px;box-shadow:0 2px 3px rgba(0,0,0,.4)}
.main-nav a{color:var(--white);font-size:9px;font-weight:700;text-decoration:none;padding:0 10px;height:32px;line-height:32px;border-right:1px solid #444}
.main-nav a.active{background:linear-gradient(#f4f4f4,#cfcfcf);color:#222;height:40px;margin-top:-8px;line-height:48px;padding:0 19px;border:none}
.main-nav a:last-child{border:none}
.sub-nav{left:277px;top:127px;width:645px;height:25px;background:linear-gradient(var(--slate-light),var(--slate));display:flex;align-items:center;padding-left:69px;z-index:2}
.sub-nav a{color:var(--white);font-size:9px;text-decoration:none;padding:0 10px;line-height:25px}
.slider{left:240px;top:120px;width:720px;height:261px;background:var(--white);border-radius:4px;box-shadow:0 1px 4px rgba(0,0,0,.3)}
.slide-photo{left:243px;top:152px;width:714px;height:168px;background:linear-gradient(#8fbbe6 0%,#b9cfe0 30%,#cdbfa8 55%,#5f7a3e 100%)}
.slide-strip{left:243px;top:320px;width:714px;height:58px;background:linear-gradient(#fafafa,#dcdcdc)}
.thumb{top:329px;width:50px;height:43px;background:var(--white);border:1px solid #ccc;padding:4px}
.thumb span{display:block;width:100%;height:100%;background:linear-gradient(#7ea6c8,#a08b6e)}
.arrow{top:341px;width:18px;height:18px}
.caption{left:245px;top:216px;width:282px;height:160px;background:linear-gradient(150deg,#6e7c9c,var(--slate-dark));transform:rotate(-2.5deg);border-radius:4px;box-shadow:2px 4px 8px rgba(0,0,0,.45);color:var(--white);padding:32px 34px 0 34px}
.caption h2{font-family:"Vollkorn",serif;font-weight:400;font-size:20px;color:#1f2840}
.caption h3{font-size:8px;font-weight:700;margin:4px 0 6px}
.caption p{font-size:8.5px;line-height:10px;color:#e4e8f0}
.caption .more{display:inline-block;margin:5px 0 0 58px;font-size:8px;color:var(--white);text-decoration:underline}
.price-tag{left:336px;top:221px;width:136px;height:24px;background:#111;border-radius:3px;color:var(--white);font-family:"Vollkorn",serif;font-size:16px;text-align:right;padding:1px 14px;z-index:3}
.listings{left:240px;top:393px;width:495px;height:507px;background:var(--white)}
.listings .divider-v{left:247px;top:0;width:1px;height:507px;background:#e6e6e6}
.listings .divider-h{left:0;top:257px;width:495px;height:1px;background:#e6e6e6}
.card{width:208px}
.card-photo{width:208px;height:108px;border:4px solid var(--white);outline:1px solid #ccc;background:linear-gradient(#7fb2e0,#c9b79a 60%,#5f7c3c)}
.card h4{font-family:"Vollkorn",serif;font-weight:400;font-size:15.5px;color:var(--title-blue);margin:6px 0 0 3px;padding-bottom:5px;border-bottom:1px solid #ccc}
.card p{font-size:9px;line-height:11.5px;color:#444;margin:4px 3px 0}
.card .foot{display:flex;justify-content:space-between;align-items:center;margin:11px 3px 0 6px}
.btn-read{background:var(--slate);color:var(--white);font-size:8px;padding:5px 10px;border-bottom:2px solid var(--accent-red)}
.card .price{font-family:"Vollkorn",serif;font-weight:600;font-size:17px;color:#222}
.finder{left:740px;top:393px;width:218px;height:240px;background:var(--dark-panel);color:var(--white);padding:17px 0 0 23px}
.finder::after{content:"";position:absolute;right:0;top:0;width:10px;height:100%;background:repeating-linear-gradient(#444 0 2px,#1a1a1a 2px 4px)}
.finder h2{font-weight:400;font-size:14.5px;width:167px;padding-bottom:5px;border-bottom:1px solid #777}
.finder label{display:block;font-size:8px;margin-top:8px}
.finder .input{width:167px;height:12px;background:var(--white);margin-top:2px}
.finder .select{height:12px;background:var(--white);margin-top:2px;position:relative}
.finder .select::after{content:"";position:absolute;right:1px;top:1px;width:12px;height:10px;background:#111}
.finder .row{display:flex;gap:22px}
.finder .row>div{width:72px}
.btn-find{display:inline-block;background:var(--accent-red);font-size:8.5px;padding:4px 8px;border-radius:3px;margin-top:10px}
.finder .hint{font-size:8px;margin-top:10px;line-height:12px}
.finder .hint u{font-weight:700}
.news{left:740px;top:633px;width:220px;height:267px;background:var(--panel);padding:18px 18px 0 23px}
.news h2{font-size:12.5px;font-weight:400;color:#222;display:flex;justify-content:space-between;align-items:center}
.news .rss{width:12px;height:11px;background:var(--rss);border-radius:2px}
.news h5{font-size:8.5px;color:var(--slate-dark);font-weight:700;margin-top:12px}
.news .meta{font-size:7.5px;color:#888;margin-top:2px}
.news p{font-size:8.5px;line-height:10.5px;color:#333;margin-top:4px}
.news .more-btn{display:block;margin:-2px 0 0 auto;width:40px;height:15px;border:1px solid #aaa;border-radius:3px;background:linear-gradient(#fff,#e2e2e2);font-size:8px;text-align:center;line-height:13px}
</style>
</head>
<body>
<div class="abs brand"><span class="brand-dot"></span>Clairvaux Homes</div>

<div class="abs search-tab"><div class="field">Searching...</div><span class="go">GO!</span></div>

<div class="abs slider"></div>
<div class="abs slide-photo" role="img" aria-label="Large stone villa with gables and garden under a blue sky"></div>
<div class="abs slide-strip"></div>
<svg class="abs arrow" style="left:589px" viewBox="0 0 18 18"><circle cx="9" cy="9" r="8" fill="#fff" stroke="#bbb"/><path d="M10.5 5.5 7 9l3.5 3.5" fill="none" stroke="#333" stroke-width="1.6"/></svg>
<div class="abs thumb" style="left:632px" role="img" aria-label="Thumbnail of a house"><span></span></div>
<div class="abs thumb" style="left:694px" role="img" aria-label="Thumbnail of a house with pool"><span></span></div>
<div class="abs thumb" style="left:756px" role="img" aria-label="Thumbnail of a pool pavilion"><span></span></div>
<div class="abs thumb" style="left:818px" role="img" aria-label="Thumbnail of a house interior"><span></span></div>
<svg class="abs arrow" style="left:889px" viewBox="0 0 18 18"><circle cx="9" cy="9" r="8" fill="#fff" stroke="#bbb"/><path d="M7.5 5.5 11 9l-3.5 3.5" fill="none" stroke="#333" stroke-width="1.6"/></svg>

<nav class="abs main-nav">
  <a class="active" href="#">HOME</a><a href="#">ABOUT US</a><a href="#">BLOG</a><a href="#">THE TEAM</a><a href="#">LOCATION</a><a href="#">IMAGE GALLERY</a><a href="#">TESTIMONIALS</a><a href="#">CONTACT AN AGENT</a>
</nav>
<nav class="abs sub-nav">
  <a href="#">Apartments</a><a href="#">Beach House</a><a href="#">City Life</a><a href="#">Mansion</a><a href="#">Modern Architecture</a><a href="#">Mountaintop</a><a href="#">Urban</a><a href="#">Wilderness</a>
</nav>

<div class="abs caption">
  <h2>Lorem ipsum dolor</h2>
  <h3>QUISQUE ELELOREM IPSUM DOLOR SIT AMET</h3>
  <p>Proin sed odio et ante adipiscing lobortis. Quisque eleLorem ipsum dolor sit amet, consectetuer adipiscing elit. Proin sed odio et ante adipiscing lobortis. Quisque eleifend, arcu a dictum varius, risus neque venenatis arcu, a semper massa mi eget ipsum.</p>
  <a class="more" href="#">READ MORE</a>
</div>
<div class="abs price-tag">$800,000</div>
<svg class="abs" style="left:354px;top:206px;z-index:4" width="26" height="26" viewBox="0 0 26 26"><path d="M6 22 13 14" stroke="#555" stroke-width="2"/><circle cx="16" cy="10" r="7" fill="#e2141b"/></svg>

<section class="abs listings">
  <div class="abs divider-v"></div>
  <div class="abs divider-h"></div>
  <article class="abs card" style="left:20px;top:16px">
    <div class="card-photo" role="img" aria-label="Brick family house with garage"></div>
    <h4>Arcu a dictum varius</h4>
    <p>Proin sed odio et ante adipiscing lobortis. Quisque eleLorem ipsum dolor sit amet, con-sectetuer adipiscing elit. Proin sed odio et ante adipiscing lobortis. Quisque eleifend, arcu a dictum varius, risus neque venenatis arcu, a semper massa mi eget ipsum.</p>
    <div class="foot"><span class="btn-read">READ MORE</span><span class="price">$799,000</span></div>
  </article>
  <article class="abs card" style="left:268px;top:16px">
    <div class="card-photo" role="img" aria-label="Mediterranean villa with terrace and palm trees"></div>
    <h4>Arcu a dictum varius</h4>
    <p>Proin sed odio et ante adipiscing lobortis. Quisque eleLorem ipsum dolor sit amet, con-sectetuer adipiscing elit. Proin sed odio et ante adipiscing lobortis. Quisque eleifend, arcu a dictum varius, risus neque venenatis arcu, a semper massa mi eget ipsum.</p>
    <div class="foot"><span class="btn-read">READ MORE</span><span class="price">$799,000</span></div>
  </article>
  <article class="abs card" style="left:20px;top:273px">
    <div class="card-photo" role="img" aria-label="Stone house with gables and garden"></div>
    <h4>Arcu a dictum varius</h4>
    <p>Proin sed odio et ante adipiscing lobortis. Quisque eleLorem ipsum dolor sit amet, con-sectetuer adipiscing elit. Proin sed odio et ante adipiscing lobortis. Quisque eleifend, arcu a dictum varius, risus neque venenatis arcu, a semper massa mi eget ipsum.</p>
    <div class="foot"><span class="btn-read">READ MORE</span><span class="price">$799,000</span></div>
  </article>
  <article class="abs card" style="left:268px;top:273px">
    <div class="card-photo" role="img" aria-label="Modern house lit at dusk with patio" style="background:linear-gradient(#4a3a2a,#c49a5a 60%,#6b5a3a)"></div>
    <h4>Arcu a dictum varius</h4>
    <p>Proin sed odio et ante adipiscing lobortis. Quisque eleLorem ipsum dolor sit amet, con-sectetuer adipiscing elit. Proin sed odio et ante adipiscing lobortis. Quisque eleifend, arcu a dictum varius, risus neque venenatis arcu, a semper massa mi eget ipsum.</p>
    <div class="foot"><span class="btn-read">READ MORE</span><span class="price">$799,000</span></div>
  </article>
</section>

<aside class="abs finder">
  <h2>Find Your Property</h2>
  <label>City &amp; State, or Zip:</label><div class="input"></div>
  <label>Search Area:</label><div class="select" style="width:167px"></div>
  <div class="row">
    <div><label>Price Range:</label><div class="select"></div></div>
    <div><label>to:</label><div class="select"></div></div>
  </div>
  <div class="row">
    <div><label>Bedroom(s):</label><div class="select"></div></div>
    <div><label>Bathroom(s):</label><div class="select"></div></div>
  </div>
  <div class="row">
    <div><label>Radius:</label><div class="select"></div></div>
    <div><span class="btn-find">Find Proposal</span></div>
  </div>
  <p class="hint">Know exactly what you want?<br>Try our &nbsp;<u>Advanced Search</u></p>
</aside>

<aside class="abs news">
  <h2>LATEST NEWS <span class="rss"></span></h2>
  <h5>Quisque eleLorem ipsum dolor sit amet</h5>
  <div class="meta">Administrator &nbsp;|&nbsp; 16:30 20/056/2011</div>
  <p>Lorem ipsum dolor sit amet, consectetuer adipiscing elit. Proin sed odio et ante adipiscing lobortis. Quisque eleLorem ipsum dolor sit amet, consectetuer adipiscing elit. Proin sed odio et ante adipiscing lobortis. Quisque eleifend</p>
  <span class="more-btn">more</span>
  <h5>Quisque eleLorem ipsum dolor sit amet</h5>
  <div class="meta">Administrator &nbsp;|&nbsp; 16:30 20/056/2011</div>
  <p>Arcu a dictum varius, risus neque venenatis arcu, a semper massa mi eget ipsum. Proin sed odio et ante adipiscing lobortis.</p>
  <span class="more-btn">more</span>
  <h5>Quisque eleLorem ipsum dolor sit amet</h5>
  <div class="meta">Administrator &nbsp;|&nbsp; 16:30 20/056/2011</div>
  <p>Lorem ipsum dolor sit amet, consectetuer adipiscing elit. Quisque eleLorem ipsum</p>
</aside>
</body>
</html>
```